Biz Card for Harrowfield Property Partners - HWPP

Harrowfield Property Partners is a commercial real estate acquisitions firm. We buy commercial property and need to raise capital from investors for each deal we buy. The vibe needs to be: give us your money, we will multiply it.
Our website: www.hrwpp-example.com
Competitors are: https://velmarholdings-example.com/, https://tribanquepartners-example.com/, http://www.ostrellecapital-example.com/
Target Market(s)
High Net Worth Individuals, Bankers, Insurance Companies, Commercial Real Estate Brokers.
Industry/Entity Type
Investment Banking
Contact Information for Business Card
Name, Title, Addess, Cell#, Office#, email, website
Requirements
Must have
- use one of our logos. See website for look and feel: www.hrwpp-example.com
Nice to have
- see website: www.hrwpp-example.com

```html
<!DOCTYPE html>
<html lang="en">
<head>
<meta charset="utf-8">
<title>Harrowfield Property Partners – Business Card</title>
<link href="https://fonts.googleapis.com/css2?family=Roboto:wght@300;400&display=swap" rel="stylesheet">
<style>
  :root {
    --backdrop: #1f1f1f;
    --navy: #0f2a47;
    --navy-deep: #0b2340;
    --navy-soft: #1d4068;
    --paper: #f1f1f1;
    --white: #ffffff;
    --ink: #132b47;
  }
  * { margin: 0; padding: 0; box-sizing: border-box; }
  html, body {
    width: 1200px; height: 1138px; overflow: hidden;
    background: var(--backdrop);
    font-family: "Roboto", Arial, sans-serif;
  }
  .card {
    position: absolute;
    width: 620px; height: 375px;
    border-radius: 14px;
    overflow: hidden;
  }
  .card-front { left: 274px; top: 186px; }
  .card-back { left: 276px; top: 608px; background: var(--paper); color: var(--ink); }

  .front-photo {
    position: absolute; inset: 0;
    background: linear-gradient(160deg, var(--navy-soft) 0%, var(--navy) 55%, var(--navy-deep) 100%);
  }
  .brand { position: absolute; display: flex; align-items: center; gap: 20px; }
  .brand-dot { border-radius: 50%; flex: none; }
  .brand-name {
    font-weight: 300; text-transform: uppercase;
    letter-spacing: 0.12em; line-height: 1.15;
  }
  .card-front .brand { left: 167px; top: 169px; }
  .card-front .brand-dot { width: 108px; height: 108px; background: var(--white); }
  .card-front .brand-name { color: var(--white); font-size: 27px; width: 300px; }
  .front-url {
    position: absolute; left: 0; right: 0; top: 330px;
    text-align: center; color: #d6dde6;
    font-size: 16px; font-weight: 300; letter-spacing: 0.3em;
  }

  .top-band {
    position: absolute; left: 0; top: 0; width: 100%; height: 100px;
    background: linear-gradient(180deg, var(--navy-deep) 0%, var(--navy) 100%);
  }
  .holder { position: absolute; left: 31px; top: 25px; color: var(--white); }
  .holder-name { font-size: 24px; font-weight: 400; }
  .holder-title { font-size: 16px; font-weight: 300; margin-top: 4px; }
  .card-back .brand { left: 224px; top: 124px; }
  .card-back .brand-dot { width: 104px; height: 104px; background: var(--navy); }
  .card-back .brand-name { color: var(--ink); font-size: 24px; width: 270px; }

  .contact { position: absolute; left: 31px; top: 270px; list-style: none; }
  .contact li { display: flex; align-items: center; gap: 12px; font-size: 17px; font-weight: 300; height: 25.5px; }
  .contact svg { width: 16px; height: 16px; fill: var(--ink); }
  .address {
    position: absolute; right: 22px; top: 295px;
    text-align: right; font-size: 17px; font-weight: 300; line-height: 25px;
    font-style: normal;
  }
</style>
</head>
<body>
  <section class="card card-front">
    <div class="front-photo" role="img" aria-label="Lighthouse under a dusky sky, tinted deep navy blue"></div>
    <div class="brand">
      <span class="brand-dot"></span>
      <span class="brand-name">Harrowfield Property Partners</span>
    </div>
    <p class="front-url">www.hrwpp-example.com</p>
  </section>

  <section class="card card-back">
    <div class="top-band" role="img" aria-label="Navy decorative wave band across the top of the card"></div>
    <div class="holder">
      <p class="holder-name">Daniel Mercer</p>
      <p class="holder-title">Managing Partner</p>
    </div>
    <div class="brand">
      <span class="brand-dot"></span>
      <span class="brand-name">Harrowfield Property Partners</span>
    </div>
    <ul class="contact">
      <li><svg viewBox="0 0 16 16"><path d="M2 6c0-2 3-3 6-3s6 1 6 3v1h-3V6H5v1H2z M4 8h8l2 5H2z"/></svg>(555) 014-2780</li>
      <li><svg viewBox="0 0 16 16"><path d="M1 3h14v10H1z M2.5 4.5 8 9l5.5-4.5v-0.5h-11z" fill-rule="evenodd"/></svg>dmercer@hrwpp-example.com</li>
      <li><svg viewBox="0 0 16 16"><circle cx="8" cy="8" r="6.5" fill="none" stroke="var(--ink)" stroke-width="1.5"/><path d="M1.5 8h13M8 1.5v13" stroke="var(--ink)" stroke-width="1.2"/></svg>www.hrwpp-example.com</li>
    </ul>
    <address class="address">418 Calloway Ave, Suite 900<br>Brightwater, FL 30000</address>
  </section>
</body>
</html>
```